Poster for a boatshow for Nautical enthusiasts, masculine and high incoming :-)

We need a poster for a boat show. Motorboats and Sailboats is presented in this Boat show (and other nautical topics like diving, wakeboard, kite, surf, fishing, ...)
This boat show is annual and the Poster is for the 2015 edition.

Your concept must be compatible in a landscape format. (We will ourselves adaptations of different formats.)
Width: 210 mm
Height: 297 mm
It's necessary for us to have the source file (vector) for make, later, the different format (flyers, website, ...)

Content of the Poster:
- 1 big picture (from a cheap stock, like Pixaloom.com) (NO CLIP ART) on full page or half page. Clip art must be a small detail added on the poster.
- Big title: « Foire fluviale des Ormeaux » (« du Léman » must be smaller of « Foire fluviale ».)
- Date: « 13, 14 et 15 novembre 2015 »
- Place: « Varimont - Genève »
- website: « www.foire-riveraine.ch » or « foire-riveraine.ch »
- Please, leave a zone in the poster for sponsors logos
- The « Jet d’eau de Genève » (http://en.wikifolio-example.org/wiki/Gerbe_Castelbrune) MUST be visible on the poster (in the picture, added like a clip art, or other graphic idea…)

Target Market(s)

Nautical enthusiasts, more masculine, high income.

Industry/Entity Type

Landscape

Font styles to use
Sans Serif

Colors
33a6d7
0892cd
ffffff

Requirements
Must have
• - The style must be modern, dynamic, bright colors, sober-minded.
• - "Jet d’eau de Genève" must be on the poster.
Should not have
• Clipart, cheap designs...
• Design with sea reference (sand, very big boats, ...). The market of the boatshow is around a lake (no sand, no boat more big of 15 meters).

```html
<!DOCTYPE html>
<html lang="fr">
<head>
<meta charset="utf-8">
<title>Foire fluviale des Ormeaux 2015</title>
<link rel="stylesheet" href="https://fonts.googleapis.com/css2?family=Josefin+Sans:wght@300;400&family=Oswald:wght@400;500&display=swap">
<style>
  :root {
    --backdrop: #000000;
    --paper: #ffffff;
    --ink: #163a4f;
    --accent: #c8161d;
    --rule: #b9c7cf;
    --sky-top: #0892cd;
    --sky-mid: #33a6d7;
    --sky-low: #9fd6d0;
    --city: #c9b79a;
    --water: #6f8fa6;
    --water-dark: #2d4150;
  }
  html, body {
    margin: 0;
    padding: 0;
    width: 1000px;
    height: 1200px;
    overflow: hidden;
    background: var(--backdrop);
  }
  .poster {
    position: absolute;
    left: 135px;
    top: 75px;
    width: 750px;
    height: 1060px;
    background: var(--paper);
    overflow: hidden;
  }
  .hero-photo {
    position: absolute;
    left: 0;
    top: 0;
    width: 750px;
    height: 580px;
    background: linear-gradient(180deg,
      var(--sky-top) 0%,
      var(--sky-mid) 30%,
      var(--sky-low) 50%,
      var(--city) 56%,
      var(--water) 66%,
      #b98f6e 78%,
      var(--water-dark) 100%);
  }
  .typeset {
    position: absolute;
    left: 0;
    top: 0;
    width: 750px;
    height: 1060px;
  }
  .title-light { font-family: "Josefin Sans", sans-serif; font-weight: 300; fill: var(--ink); }
  .title-main { font-family: "Josefin Sans", sans-serif; font-weight: 400; fill: var(--ink); }
  .venue, .dates { font-family: "Oswald", sans-serif; fill: var(--accent); }
  .venue-city { font-weight: 500; }
  .website { font-family: "Oswald", sans-serif; font-weight: 400; fill: var(--ink); }
  .website-sep { fill: var(--accent); }
  .sponsor-name { font-family: "Oswald", sans-serif; font-weight: 500; fill: var(--ink); }
</style>
</head>
<body>
  <main class="poster">
    <div class="hero-photo" role="img" aria-label="Photographie d’un port de plaisance au soleil couchant : voiliers et vedette à quai, immeubles au bord de l’eau et la Gerbe de Castelbrune jaillissant à gauche"></div>

    <svg class="typeset" viewBox="0 0 750 1060" xmlns="http://www.w3.org/2000/svg">
      <!-- Event title -->
      <text class="title-light" x="113" y="695" font-size="80" textLength="420" lengthAdjust="spacing">FOIRE</text>
      <text class="title-main" x="111" y="793" font-size="108" textLength="524" lengthAdjust="spacingAndGlyphs">FLUVIALE</text>
      <text class="title-light" x="113" y="855" font-size="66" textLength="420" lengthAdjust="spacingAndGlyphs">DES ORMEAUX</text>

      <!-- Venue -->
      <text class="venue" x="553" y="665" font-size="36" textLength="84" lengthAdjust="spacingAndGlyphs">VARIMONT</text>
      <text class="venue venue-city" x="553" y="697" font-size="36" textLength="84" lengthAdjust="spacingAndGlyphs">GENÈVE</text>

      <!-- Dates -->
      <text class="dates" x="553" y="830" font-size="27" textLength="84" lengthAdjust="spacingAndGlyphs">13.14 . 15</text>
      <text class="dates" x="553" y="855" font-size="27" textLength="84" lengthAdjust="spacingAndGlyphs">NOV 2015</text>

      <!-- Website -->
      <text class="website" x="375" y="934" font-size="19" text-anchor="middle">WWW.FOIRE-RIVERAINE.CH <tspan class="website-sep" dx="6">I</tspan><tspan dx="6">FOIRE-RIVERAINE.CH</tspan></text>
      <line x1="73" y1="948" x2="690" y2="948" stroke="var(--rule)" stroke-width="1.5"/>

      <!-- Sponsors -->
      <g class="sponsors">
        <text class="sponsor-name" x="240" y="1005" font-size="22" text-anchor="middle">BRISANT</text>
        <circle cx="365" cy="981" r="9" fill="var(--sky-top)"/>
        <text class="sponsor-name" x="365" y="1012" font-size="18" text-anchor="middle">VALTURA</text>
        <rect x="445" y="982" width="11" height="11" fill="var(--ink)"/>
        <text class="sponsor-name" x="500" y="994" font-size="15" text-anchor="middle" dx="6">CORVEL MOTEURS</text>
      </g>
    </svg>
  </main>
</body>
</html>
```